Dune Air & Plus business card

I need an awesome, double-sided business card designed with our new logo. I would like the one side black with the colored logo, and the back side is all yours. I'd like to see horizontal and vertical layouts. Get creative! Thank you.

Target Market(s)

HVAC, Heating and Cooling in Phoenix, AZ

Industry/Entity Type

HVAC

Contact Information for Business Card

We need our new logo on the card. Tom Harker, (623) 555-0142, tom@trydunesair.com, www.trydunesair.com, ROC 514273

```html
<!DOCTYPE html>
<html lang="en">
<head>
<meta charset="UTF-8">
<title>Dune Air &amp; Plus — Business Card</title>
<link href="https://fonts.googleapis.com/css2?family=Montserrat:wght@400;500;800&display=swap" rel="stylesheet">
<style>
  :root {
    --stage: #2b2b2d;
    --card: #1f1f21;
    --blue: #2f86d6;
    --orange: #f08a2a;
    --white: #f2f2f2;
    --pattern-light: #47474b;
    --pattern-mid: #2a2a2d;
    --pattern-dark: #0f0f10;
  }
  * { box-sizing: border-box; margin: 0; padding: 0; }
  html, body { width: 1200px; height: 900px; overflow: hidden; }
  body {
    background: var(--stage);
    font-family: "Montserrat", sans-serif;
    color: var(--white);
    position: relative;
  }
  .card {
    position: absolute;
    top: 90px;
    width: 420px;
    height: 720px;
    border-radius: 36px;
    background: var(--card);
    overflow: hidden;
    box-shadow: 0 20px 40px rgba(0,0,0,0.45);
  }
  .card-front { left: 150px; }
  .card-back  { left: 630px; background: var(--pattern-dark); }

  .brand {
    position: absolute;
    top: 150px;
    left: 0; right: 0;
    display: flex;
    align-items: center;
    justify-content: center;
    gap: 14px;
  }
  .brand-mark {
    width: 34px; height: 34px;
    border-radius: 50%;
    background: var(--orange);
  }
  .brand-name {
    font-weight: 800;
    font-size: 38px;
    color: var(--blue);
    letter-spacing: 0.5px;
  }

  .person { position: absolute; top: 330px; left: 0; right: 0; text-align: center; }
  .person-name { font-weight: 800; font-size: 36px; color: var(--blue); }
  .person-role { font-weight: 400; font-size: 18px; margin-top: 6px; }

  .icon-row {
    position: absolute; top: 430px; left: 40px; right: 40px;
    display: flex; align-items: center; gap: 10px;
  }
  .rule { flex: 1; height: 2px; background: var(--orange); }
  .icon {
    width: 38px; height: 38px; border-radius: 8px;
    background: var(--orange);
    display: flex; align-items: center; justify-content: center;
  }
  .icon svg { width: 22px; height: 22px; }

  .contact { position: absolute; top: 505px; left: 0; right: 0; text-align: center; font-size: 18px; line-height: 32px; }
  .contact .accent { color: var(--orange); }
  .short-rule { position: absolute; top: 625px; left: 160px; width: 100px; height: 2px; background: var(--orange); }
  .licence { position: absolute; top: 650px; left: 0; right: 0; text-align: center; font-size: 18px; }

  .back-pattern {
    position: absolute; inset: 0;
    background:
      radial-gradient(ellipse at 20% 8%, rgba(90,90,96,0.55), transparent 55%),
      linear-gradient(160deg, var(--pattern-light) 0%, var(--pattern-mid) 40%, var(--pattern-dark) 100%);
  }
  .back-brand {
    position: absolute; top: 300px; left: 0; right: 0;
    display: flex; align-items: center; justify-content: center; gap: 12px;
  }
  .back-brand .brand-mark { width: 28px; height: 28px; }
  .back-brand .brand-name { font-size: 30px; }
</style>
</head>
<body>
  <section class="card card-front">
    <div class="brand">
      <span class="brand-mark"></span>
      <span class="brand-name">Dune Air &amp; Plus</span>
    </div>

    <div class="person">
      <p class="person-name">Tom Harker</p>
      <p class="person-role">CEO &amp; Founder</p>
    </div>

    <div class="icon-row">
      <span class="rule"></span>
      <span class="icon" aria-label="Phone">
        <svg viewBox="0 0 24 24" fill="#fff"><path d="M6.6 10.8a15 15 0 0 0 6.6 6.6l2.2-2.2a1 1 0 0 1 1-.25 11.4 11.4 0 0 0 3.6.6 1 1 0 0 1 1 1V20a1 1 0 0 1-1 1A17 17 0 0 1 3 4a1 1 0 0 1 1-1h3.5a1 1 0 0 1 1 1c0 1.25.2 2.45.6 3.6a1 1 0 0 1-.25 1z"/></svg>
      </span>
      <span class="icon" aria-label="Email">
        <svg viewBox="0 0 24 24" fill="#fff"><path d="M3 5h18v14H3z"/><path d="M3 5l9 7 9-7" fill="none" stroke="#f08a2a" stroke-width="2"/></svg>
      </span>
      <span class="icon" aria-label="Website">
        <svg viewBox="0 0 24 24" fill="none" stroke="#fff" stroke-width="2"><circle cx="12" cy="12" r="9"/><path d="M3 12h18M12 3c3 3.5 3 14.5 0 18M12 3c-3 3.5-3 14.5 0 18"/></svg>
      </span>
      <span class="rule"></span>
    </div>

    <div class="contact">
      <p>(623) 555-0142</p>
      <p>tom@trydunesair.com</p>
      <p>www.<span class="accent">trydunesair</span>.com</p>
    </div>
    <span class="short-rule"></span>
    <p class="licence">ROC 514273</p>
  </section>

  <section class="card card-back">
    <div class="back-pattern" role="img" aria-label="Tonal repeating pattern of the company emblem, lighter grey at the top fading to black"></div>
    <div class="back-brand">
      <span class="brand-mark"></span>
      <span class="brand-name">Dune Air &amp; Plus</span>
    </div>
  </section>
</body>
</html>
```